UK Based Internet hosting Company wants a vibrant eCommerce site designed.

We have only just had our logo and brand designed by Pixel Forum which went so well that we would like to open up our website design project on here too.

The company is called 'Quay Server Lantern' and we provide a range of website hosting, dedicated server, domain name and email solutions that people will be able to purchase online in neatly packaged options from the outset.

Our logo and brand is bright turquoise, black & white (samples of branding will be attached with this project) but we would like the website to be very vibrant with good use of white space rather than a black website.

We want to appeal to end users so web designers, developers and people who would like to host their website. But we also want to appeal to resellers that would like to resell our hosting packages too.

We want a big push on social media and blogging on the site as we would like our brand to be 100% up with Chatterleaf, Murmel, workLoop, Vidplume and Zorbix+. It would be great to have this integrated into the site with share buttons and rating buttons etc.

We would like to see a homepage initially with a view to providing several page layers down to help our in-house developers hook in our back-end into this front end effectively.

Great customer experience and an easy to navigate journey to the checkout when purchasing the hosting packages is paramount !!

We like how the following sites are set-out and presented:

www.brightmarrow.uk
http://www.tallyfold.co.uk
https://www.qv7.net/web-hosting/

Target Market(s)

We have 3 target markets.

Target market 1 - end users, consumers such as Web Designers, Developers and small businesses.

Target Market 2 - Resellers, small businesses that would like to resell our services.

Target Market 3 - Medium to large businesses that would like more of a bespoke solution.

Industry/Entity Type

Internet

Requirements
Must have
• Colourful, bright, bold, easy to navigate and to purchase packages.
• Plenty of call to actions, social media, ratings.
• Video case studies and testimonials would be nice.

```html
<!DOCTYPE html>
<html lang="en">
<head>
<meta charset="utf-8">
<title>Quay Server Lantern – Web Hosting</title>
<link href="https://fonts.googleapis.com/css2?family=Raleway:wght@300;400;600;700;800&family=Open+Sans:wght@400;600;700&display=swap" rel="stylesheet">
<style>
:root{
  --teal:#1fc7c9;
  --teal-deep:#12aab6;
  --mint:#1ec995;
  --mint-alt:#23d19f;
  --ink:#2b2b2b;
  --ink-deep:#1d1d1d;
  --dark-band:#333436;
  --text:#555;
  --muted:#8a8a8a;
  --line:#e2e2e2;
  --white:#fff;
  --red:#c9262b;
}
*{box-sizing:border-box;margin:0;padding:0}
html,body{width:1200px;height:4444px;overflow:hidden}
body{font-family:"Open Sans",Arial,sans-serif;color:var(--text);background:var(--white);font-size:14px;line-height:1.55}
.wrap{width:1004px;margin:0 auto;position:relative}
h1,h2,h3,h4{font-family:Raleway,Arial,sans-serif}

/* header */
.site-header{height:98px;position:relative}
.site-header .wrap{height:98px}
.brand{position:absolute;left:0;top:12px;display:flex;align-items:center;gap:12px}
.brand-dot{width:58px;height:58px;border-radius:50%;background:var(--teal)}
.brand-name{font-family:Raleway,Arial,sans-serif;font-weight:600;font-size:22px;line-height:1.1;color:var(--ink);width:150px}
.top-links{position:absolute;right:0;top:6px;font-size:12px;color:var(--muted)}
.top-links span{margin:0 6px}
.main-nav{position:absolute;right:0;top:62px;display:flex;gap:38px;font-size:14px;color:var(--ink)}

/* hero */
.hero{height:524px;background:linear-gradient(180deg,var(--teal-deep),var(--teal) 60%,#27d2d4);color:var(--white);text-align:center;position:relative}
.hero h1{font-size:54px;font-weight:700;padding-top:36px;letter-spacing:.5px}
.hero p{font-size:16px;margin-top:2px}
.hero-visual{position:absolute;left:340px;top:190px;width:520px;height:300px;border-radius:4px;background:linear-gradient(180deg,#2c2c2e,#0f0f10 70%,#1a8f95)}

/* domain search */
.domain-bar{height:154px;background:var(--dark-band);text-align:center;padding-top:30px}
.domain-form{display:inline-flex;width:520px;height:50px;background:var(--white)}
.domain-form .field{flex:1;text-align:left;padding:0 22px;line-height:50px;color:#aaa;font-size:14px}
.domain-form .btn{width:100px;background:var(--teal);color:var(--white);line-height:50px;font-size:15px}
.tlds{margin-top:22px;font-size:20px;color:var(--white)}
.tlds b{color:var(--teal);font-weight:400;margin-right:16px}
.tlds i{font-style:normal;margin:0 10px;color:#999}

/* section heading rule */
.rule{height:1px;background:var(--line);position:relative}
.rule::before{content:"";position:absolute;left:10px;top:-1px;width:50px;height:3px;background:var(--mint)}

/* welcome */
.welcome{height:261px;padding-top:40px}
.welcome-row{display:flex;gap:30px;height:160px}
.welcome-title{width:260px;border-right:1px solid var(--line)}
.welcome-title h2{font-weight:300;font-size:32px;color:var(--ink);letter-spacing:1px}
.welcome-title .brand-inline{display:flex;align-items:center;gap:12px;margin-top:10px}
.welcome p{flex:1;font-size:14px;color:var(--muted);line-height:1.6}

/* plan boxes */
.offers{display:flex;height:300px;margin-bottom:35px}
.offer{flex:1;background:var(--mint);color:var(--white);text-align:center;position:relative;padding-top:24px}
.offer:nth-child(2){background:var(--mint-alt)}
.offer::after{content:"";position:absolute;left:50%;bottom:-24px;margin-left:-24px;border:24px solid transparent;border-bottom:0}
.offer:nth-child(1)::after,.offer:nth-child(3)::after{border-top-color:var(--mint)}
.offer:nth-child(2)::after{border-top-color:var(--mint-alt)}
.offer svg{width:100px;height:84px}
.offer small{display:block;font-size:12px;letter-spacing:1px;margin-top:8px}
.offer .price{font-family:Raleway,Arial,sans-serif;font-size:34px;font-weight:700;line-height:1.2}
.offer h3{font-size:25px;font-weight:600;letter-spacing:.5px}
.offer p{font-size:13px;font-weight:600;width:240px;margin:4px auto 0;line-height:1.45}

/* dark sections */
.dark-band{background:linear-gradient(120deg,#4a4b4d,#222 45%,#3a3b3d 80%,#1a1a1a);color:var(--white)}
.section-head{display:flex;gap:20px;padding-top:40px;height:170px}
.section-head .title{width:280px}
.section-head h2{font-weight:300;font-size:33px;letter-spacing:1px;line-height:1.1;text-transform:uppercase}
.section-head h2 strong{display:block;font-weight:700;font-size:64px;color:var(--mint);letter-spacing:2px;line-height:1.05}
.section-head p{flex:1;font-size:13.5px;line-height:1.55;padding-top:4px}
.light .section-head h2{color:var(--ink)}
.light .section-head p{color:var(--muted)}

.plans{height:700px}
.plans .rule{background:#555}
.plan-grid{display:flex;gap:16px;margin-top:48px}
.plan{flex:1;background:var(--white);color:var(--ink);text-align:center;height:412px;padding:22px 18px 0}
.plan.featured{background:var(--mint);color:var(--white)}
.plan h3{font-size:38px;font-weight:600}
.plan .cost{font-family:Raleway,Arial,sans-serif;font-size:40px;font-weight:600;margin:6px 0 6px}
.plan .cost span{font-size:18px;font-weight:400;margin-left:6px}
.plan ul{list-style:none;font-size:14px}
.plan li{border-top:1px solid #ddd;line-height:40px}
.plan.featured li{border-top-color:rgba(255,255,255,.35)}
.plan .cta{display:inline-block;margin-top:10px;width:110px;line-height:36px;background:var(--mint);color:var(--white);font-size:16px}
.plan.featured .cta{background:var(--white);color:var(--mint)}

/* features */
.features{height:643px}
.feature-grid{display:grid;grid-template-columns:1fr 1fr;gap:34px 70px;margin-top:50px;padding:0 10px}
.feature{display:flex;gap:24px}
.feature svg{width:56px;height:56px;flex:none;fill:#888}
.feature h4{font-family:"Open Sans",Arial,sans-serif;font-size:18px;color:var(--ink);font-weight:700}
.feature p{font-size:13px;color:var(--muted);line-height:1.55;margin-top:8px}

/* services */
.services{height:657px;margin-top:9px}
.services .rule{background:#555}
.service-grid{display:flex;gap:16px;margin-top:76px}
.service{flex:1;background:var(--white);color:var(--ink);text-align:center;height:340px;padding:18px 14px 0;position:relative}
.service::after{content:"";position:absolute;left:50%;bottom:-20px;margin-left:-20px;border:20px solid transparent;border-bottom:0;border-top-color:var(--white)}
.service.featured{background:var(--mint);color:var(--white)}
.service.featured::after{border-top-color:var(--mint)}
.service svg{width:90px;height:90px}
.service h3{font-size:21px;font-weight:700;margin-top:4px;white-space:nowrap}
.service p{font-size:13px;line-height:1.45;margin-top:6px}
.service.featured p{font-weight:700}
.service .more{display:block;font-weight:700;font-size:13px;margin-top:12px}

/* testimonials */
.clients{height:548px}
.quote{position:absolute;display:flex;align-items:center;gap:18px}
.quote .face{width:148px;height:148px;border-radius:50%;border:9px solid var(--mint);background:linear-gradient(160deg,#e9e6e2,#b9b1aa)}
.quote.second .face{border-color:var(--ink)}
.quote h4{font-family:"Open Sans",Arial,sans-serif;font-size:16px;color:var(--ink)}
.quote .role{font-size:13px;color:var(--ink)}
.quote .role b{color:var(--mint);font-weight:400}
.quote p{font-size:13px;color:var(--ink);width:300px;margin-top:12px;line-height:1.5}
.quote.first{left:-20px;top:220px;text-align:right}
.quote.second{left:393px;top:345px}

/* footer */
.site-footer{height:454px;background:var(--ink);color:#bbb;padding-top:30px}
.footer-cols{display:flex;gap:40px}
.footer-about{width:330px;font-size:12px}
.footer-about .brand-inline{display:flex;align-items:center;gap:12px}
.footer-about .brand-dot{width:48px;height:48px}
.footer-about .brand-name{color:var(--white);font-size:18px}
.footer-about p{margin-top:16px;line-height:1.5}
.footer-about h4{font-family:"Open Sans",Arial,sans-serif;font-weight:400;font-size:15px;color:#ccc;margin-top:36px;padding-top:18px;border-top:1px solid #444}
.newsletter{display:flex;margin-top:22px;height:32px;width:330px}
.newsletter .field{flex:1;background:var(--white);color:#888;line-height:32px;padding:0 10px;font-size:12px}
.newsletter .btn{width:100px;background:var(--red);color:var(--white);text-align:center;line-height:32px;font-size:12px;font-weight:700}
.socials{display:flex;gap:14px;margin-top:30px}
.socials span{width:60px;height:60px;border-radius:50%;border:2px solid #ccc;display:flex;align-items:center;justify-content:center;font-size:10px;color:#ddd}
.footer-links{width:140px;font-size:12px;line-height:1.55}
.footer-links h4{font-family:"Open Sans",Arial,sans-serif;font-size:13px;font-weight:400;color:#ddd;margin-bottom:6px;padding-bottom:6px;border-bottom:1px solid #444}
.footer-links ul{list-style:none;margin-bottom:26px}
.footer-blog{flex:1}
.footer-blog h4{background:#3c3c3c;color:var(--white);font-family:"Open Sans",Arial,sans-serif;font-size:13px;font-weight:700;padding:6px 12px}
.post-main{display:flex;gap:24px;margin-top:20px}
.post-main .thumb{width:112px;height:112px;background:linear-gradient(150deg,#5a1418,#2a0a0c)}
.post-main h5{font-size:14px;color:#ddd;font-weight:400}
.post-main p{font-size:12px;color:#999;margin-top:8px;line-height:1.5}
.post-mini{display:flex;gap:60px;margin-top:40px;font-size:12px;color:#aaa}
.post-mini div{display:flex;gap:12px;align-items:center}
.post-mini i{width:48px;height:48px;background:linear-gradient(150deg,#5a4a8a,#2a2050)}
.footer-bottom{height:35px;background:var(--ink-deep);color:#aaa;font-size:11px}
.footer-bottom .wrap{display:flex;justify-content:space-between;line-height:35px}
</style>
</head>
<body>

<header class="site-header">
  <div class="wrap">
    <div class="brand"><span class="brand-dot"></span><span class="brand-name">Quay Server Lantern</span></div>
    <div class="top-links">Login <span>|</span> Register <span>|</span> Country</div>
    <nav class="main-nav"><span>Home</span><span>Layouts</span><span>Domains</span><span>Hosting</span><span>Elements</span><span>Pages</span><span>Portfolio</span><span>Contact</span></nav>
  </div>
</header>

<section class="hero">
  <h1>Reliable and Affordable Web Hosting</h1>
  <p>Lorem Ipsum has been the industry's standard dummy text ever since the 1500s, when an unknown printer.</p>
  <div class="hero-visual" role="img" aria-label="Row of black server towers"></div>
</section>

<section class="domain-bar">
  <div class="domain-form"><span class="field">Enter Your Domain Name Here</span><span class="btn">Search</span></div>
  <div class="tlds"><b>Top Domains</b>.com $11.99 <i>|</i> .org $11.99 <i>|</i> .net $10.99</div>
</section>

<section class="welcome">
  <div class="wrap">
    <div class="welcome-row">
      <div class="welcome-title">
        <h2>WELCOME TO</h2>
        <div class="brand-inline"><span class="brand-dot"></span><span class="brand-name">Quay Server Lantern</span></div>
      </div>
      <p>Lorem Ipsum has been the industry's standard dummy text ever since the 1500s, when an unknown printer took a galley of type and scrambled it to make a type specimen book. It has survived not only five centuries, but also the leap into electronic typesetting, remaining essentially unchanged. It was popularised in the 1960s with the release of Letraset sheets containing Lorem Ipsum passages, and more recently with desktop publishing software like Aldus PageMaker including versions of Lorem Ipsum.</p>
    </div>
    <div class="rule"></div>
  </div>
</section>

<div class="wrap">
  <div class="offers">
    <div class="offer">
      <svg viewBox="0 0 100 84" fill="none" stroke="#fff" stroke-width="4"><circle cx="50" cy="24" r="14"/><path d="M24 80v-10a26 26 0 0 1 52 0v10z"/><circle cx="22" cy="32" r="9"/><circle cx="78" cy="32" r="9"/><path d="M4 70a18 18 0 0 1 22-18M96 70a18 18 0 0 0-22-18"/></svg>
      <small>STARTING AT</small><div class="price">$ 16.99</div><h3>RESELLER HOSTING</h3>
      <p>Lorem Ipsum has been the industry's standard dummy text ever</p>
    </div>
    <div class="offer">
      <svg viewBox="0 0 100 84" fill="none" stroke="#fff" stroke-width="4"><path d="M22 66a16 16 0 0 1 2-32 24 24 0 0 1 46-6 18 18 0 0 1 8 36z"/><rect x="38" y="40" width="24" height="30" fill="#fff"/><path d="M42 48h16M42 56h16M42 64h16" stroke="#23d19f" stroke-width="3"/></svg>
      <small>STARTING AT</small><div class="price">$ 16.99</div><h3>VPS HOSTING</h3>
      <p>Lorem Ipsum has been the industry's standard dummy text ever</p>
    </div>
    <div class="offer">
      <svg viewBox="0 0 100 84" fill="none" stroke="#fff" stroke-width="4"><rect x="24" y="4" width="52" height="18" rx="3"/><rect x="24" y="30" width="52" height="18" rx="3"/><rect x="24" y="56" width="52" height="18" rx="3"/><circle cx="34" cy="13" r="2" fill="#fff"/><circle cx="34" cy="39" r="2" fill="#fff"/><circle cx="34" cy="65" r="2" fill="#fff"/><path d="M50 74v8M30 82h40"/></svg>
      <small>STARTING AT</small><div class="price">$ 16.99</div><h3>DEDICATED SERVERS</h3>
      <p>Lorem Ipsum has been the industry's standard dummy text ever</p>
    </div>
  </div>
</div>

<section class="plans dark-band">
  <div class="wrap">
    <div class="section-head">
      <div class="title"><h2>Most Popular <strong>PLANS</strong></h2></div>
      <p>Lorem Ipsum has been the industry's standard dummy text ever since the 1500s, when an unknown printer took a galley of type and scrambled it to make a type specimen book. It has survived not only five centuries, but also the leap into electronic typesetting</p>
    </div>
    <div class="rule"></div>
    <div class="plan-grid">
      <div class="plan featured"><h3>Basic</h3><div class="cost">$9.99<span>/mo</span></div><ul><li>1 GB Bandwidth</li><li>256 MB Memory</li><li>24/7 Full Support</li><li>Free Domain Name</li><li>Money back Guarantee</li></ul><span class="cta">Sign Up</span></div>
      <div class="plan"><h3>Standard</h3><div class="cost">$28.9<span>/mo</span></div><ul><li>1 GB Bandwidth</li><li>256 MB Memory</li><li>24/7 Full Support</li><li>Free Domain Name</li><li>Money back Guarantee</li></ul><span class="cta">Sign Up</span></div>
      <div class="plan"><h3>Premium</h3><div class="cost">$38.9<span>/mo</span></div><ul><li>1 GB Bandwidth</li><li>256 MB Memory</li><li>24/7 Full Support</li><li>Free Domain Name</li><li>Money back Guarantee</li></ul><span class="cta">Sign Up</span></div>
      <div class="plan"><h3>Unlimited</h3><div class="cost">$68.9<span>/mo</span></div><ul><li>1 GB Bandwidth</li><li>256 MB Memory</li><li>24/7 Full Support</li><li>Free Domain Name</li><li>Money back Guarantee</li></ul><span class="cta">Sign Up</span></div>
    </div>
  </div>
</section>

<section class="features light">
  <div class="wrap">
    <div class="section-head">
      <div class="title"><h2>Our Excellent <strong>FEATURES</strong></h2></div>
      <p>Lorem Ipsum has been the industry's standard dummy text ever since the 1500s, when an unknown printer took a galley of type and scrambled it to make a type specimen book. It has survived not only five centuries, but also the leap into electronic typesetting, remaining essentially unchanged. It was popularised in the 1960s with the release of Letraset sheets containing Lorem Ipsum passages, and more recently with desktop.</p>
    </div>
    <div class="rule"></div>
    <div class="feature-grid">
      <div class="feature"><svg viewBox="0 0 56 56"><path d="M24 4h8l1 7 5 2 6-4 6 6-4 6 2 5 7 1v8l-7 1-2 5 4 6-6 6-6-4-5 2-1 7h-8l-1-7-5-2-6 4-6-6 4-6-2-5-7-1v-8l7-1 2-5-4-6 6-6 6 4 5-2z"/><circle cx="28" cy="28" r="8" fill="#fff"/></svg><div><h4>Loads of Settings</h4><p>Lorem Ipsum has been the industry's standard dummy text ever since the 1500s, when an unknown printer took a galley of type and scrambled it to make</p></div></div>
      <div class="feature"><svg viewBox="0 0 56 56"><path d="M14 44a11 11 0 0 1 1-22 15 15 0 0 1 29-2 12 12 0 0 1 2 24z"/></svg><div><h4>Hosting In The Cloud</h4><p>Lorem Ipsum has been the industry's standard dummy text ever since the 1500s, when an unknown printer took a galley of type and scrambled it to make</p></div></div>
      <div class="feature"><svg viewBox="0 0 56 56"><path d="M12 8h32l6 30H6z"/><rect x="6" y="38" width="44" height="12" rx="2"/><circle cx="42" cy="44" r="2" fill="#fff"/></svg><div><h4>Unlimited Disk Space</h4><p>Lorem Ipsum has been the industry's standard dummy text ever since the 1500s, when an unknown printer took a galley of type and scrambled it to make</p></div></div>
      <div class="feature"><svg viewBox="0 0 56 56"><circle cx="28" cy="28" r="24"/><circle cx="28" cy="28" r="18" fill="#fff"/><path d="M28 30l10-12 2 2-10 12z"/><circle cx="28" cy="30" r="4"/></svg><div><h4>Amazing Performance Servers</h4><p>Lorem Ipsum has been the industry's standard dummy text ever since the 1500s, when an unknown printer took a galley of type and scrambled it to make</p></div></div>
      <div class="feature"><svg viewBox="0 0 56 56"><path d="M20 10h16v6h14v32H6V16h14zm4 2v4h8v-4z"/><rect x="6" y="28" width="44" height="3" fill="#fff"/></svg><div><h4>Business Hosting Solutions</h4><p>Lorem Ipsum has been the industry's standard dummy text ever since the 1500s, when an unknown printer took a galley of type and scrambled it to make</p></div></div>
      <div class="feature"><svg viewBox="0 0 56 56"><path d="M8 32a20 20 0 0 1 40 0v14h-4V32a16 16 0 0 0-32 0v14H8z"/><rect x="6" y="30" width="12" height="20" rx="3"/><rect x="38" y="30" width="12" height="20" rx="3"/></svg><div><h4>24/7 Live Support</h4><p>Lorem Ipsum has been the industry's standard dummy text ever since the 1500s, when an unknown printer took a galley of type and scrambled it to make</p></div></div>
    </div>
  </div>
</section>

<section class="services dark-band">
  <div class="wrap">
    <div class="section-head">
      <div class="title"><h2>Our Top Most <strong>SERVICES</strong></h2></div>
      <p>Lorem Ipsum has been the industry's standard dummy text ever since the 1500s, when an unknown printer took a galley of type and scrambled it to make a type specimen book. It has survived not only five centuries, but also the leap into electronic typesetting, remaining essentially unchanged. It was popularised in the 1960s with the release of Letraset</p>
    </div>
    <div class="rule"></div>
    <div class="service-grid">
      <div class="service featured">
        <svg viewBox="0 0 96 96" fill="none" stroke="#fff" stroke-width="4"><rect x="10" y="18" width="76" height="58" rx="4"/><path d="M10 32h76"/><circle cx="20" cy="25" r="2" fill="#fff"/><circle cx="28" cy="25" r="2" fill="#fff"/><circle cx="62" cy="60" r="10"/><path d="M62 44v6M62 70v6M46 60h6M72 60h6"/></svg>
        <h3>Web Sites manage</h3><p>Lorem Ipsum has been the industry's standard dummy text ever since the 1500s, when an unknown printer took a galley of type and scrambled it to make a type specimen book</p><span class="more">Readmore</span>
      </div>
      <div class="service">
        <svg viewBox="0 0 96 96" fill="none" stroke="#555" stroke-width="4"><circle cx="48" cy="48" r="36"/><ellipse cx="48" cy="48" rx="16" ry="36"/><path d="M14 34h68M14 62h68"/><rect x="8" y="40" width="80" height="16" fill="#fff" stroke="none"/><text x="48" y="54" text-anchor="middle" font-family="Raleway,Arial,sans-serif" font-size="15" font-weight="700" fill="#555" stroke="none">WWW</text></svg>
        <h3>Domain Service</h3><p>Lorem Ipsum has been the industry's standard dummy text ever since the 1500s, when an unknown printer took a galley of type and scrambled it to make a type specimen book</p><span class="more">Readmore</span>
      </div>
      <div class="service">
        <svg viewBox="0 0 96 96" fill="none" stroke="#555" stroke-width="4"><rect x="10" y="22" width="76" height="52" rx="3"/><path d="M10 24l38 30 38-30M10 72l28-24M86 72L58 48"/></svg>
        <h3>Email Service</h3><p>Lorem Ipsum has been the industry's standard dummy text ever since the 1500s, when an unknown printer took a galley of type and scrambled it to make a type specimen book</p><span class="more">Readmore</span>
      </div>
      <div class="service">
        <svg viewBox="0 0 96 96" fill="none" stroke="#555" stroke-width="4"><circle cx="48" cy="48" r="36"/><path d="M30 66V56M42 66V48M54 66V42M66 66V32" stroke-width="7"/><path d="M28 46l14-12 10 6 16-14"/></svg>
        <h3>Marketing Service</h3><p>Lorem Ipsum has been the industry's standard dummy text ever since the 1500s, when an unknown printer took a galley of type and scrambled it to make a type specimen book</p><span class="more">Readmore</span>
      </div>
    </div>
  </div>
</section>

<section class="clients light">
  <div class="wrap">
    <div class="section-head">
      <div class="title"><h2>Our Clints <strong>SAYS</strong></h2></div>
      <p>Lorem Ipsum has been the industry's standard dummy text ever since the 1500s, when an unknown printer took a galley of type and scrambled it to make a type specimen book. It has survived not only five centuries, but also the leap into electronic typesetting, remaining essentially unchanged. It was popularised in the 1960s with the release of Letraset sheets containing Lorem Ipsum passages, and more recently with desktop.</p>
    </div>
    <div class="rule"></div>
    <div class="quote first">
      <div><h4>Rowan Pellby</h4><div class="role">Marketing - <b>Brightvane</b></div><p>Lorem ipsum dolor sit amet, consectetuer adipiscing elit et justo sit Suspendisse et justo.</p></div>
      <div class="face" role="img" aria-label="Client portrait photo"></div>
    </div>
    <div class="quote second">
      <div class="face" role="img" aria-label="Client portrait photo"></div>
      <div><h4>Rowan Pellby</h4><div class="role">Marketing - <b>Brightvane</b></div><p>Lorem ipsum dolor sit amet, consectetuer adipiscing elit et justo sit Suspendisse et justo.</p></div>
    </div>
  </div>
</section>

<footer class="site-footer">
  <div class="wrap footer-cols">
    <div class="footer-about">
      <div class="brand-inline"><span class="brand-dot"></span><span class="brand-name">Quay Server Lantern</span></div>
      <p>We make registering, hosting, and managing domains for yourself or others easy and affordable, because the internet needs people.</p>
      <h4>Join The Newsletter</h4>
      <div class="newsletter"><span class="field">Email</span><span class="btn">SUBSCRIBE</span></div>
      <div class="socials"><span>Murmel</span><span>Chatterleaf</span><span>Zorbix+</span><span>workLoop</span></div>
    </div>
    <div class="footer-links">
      <h4>Footer Links</h4>
      <ul><li>Registration</li><li>Transfer</li><li>New TLDs</li><li>Personal Domain</li></ul>
      <h4>Footer Links</h4>
      <ul><li>Support</li><li>Dedicated Server</li><li>Virtual Server</li><li>Shared Hosting</li><li>Clients</li></ul>
    </div>
    <div class="footer-blog">
      <h4>FROM THE BLOG</h4>
      <div class="post-main">
        <div class="thumb" role="img" aria-label="Blog post image"></div>
        <div><h5>Best Way to Speed Up Loading</h5><p>Starting out by clearing cache, lorem ipsum dolor sit consectetur elit. Maecenas ac erat dui. Nulla fuis.</p></div>
      </div>
      <div class="post-mini">
        <div><i role="img" aria-label="Blog post thumbnail"></i><span>Another Blog Post Title<br>Here</span></div>
        <div><i role="img" aria-label="Blog post thumbnail"></i><span>Post a Neat Short Lazy<br>Offer</span></div>
      </div>
    </div>
  </div>
</footer>
<div class="footer-bottom"><div class="wrap"><span>© WebsiteName</span><span>To Top ▲</span></div></div>

</body>
</html>
```